Keystride Sport And Fitness- Rates

I am opening up a new Gym/Training Facility. The Name of my New gym is Keystride Sports And Fitness. I am wanting to design a card that captures Membership Pricing/Personal Training Pricing. I will Upload the Logo. My colors are Red/Black/Silver. I really want there pricing card to "POP". IT needs to be very Professional and Clean. I will be placing these cards on a 5'7 . I would like these item on the card:
Name of Company: Keystride Sports And Fitness
Address:
2817 Wexley Commerce Dr.
Suite 312 Chantilly, VA 20418
Phone #: 703-555-0186
website: www.keystridesnf.example
Membership Rates:
$99/Month
$49 Heroes Rate
Family Plan:
2 People $149
3 People $199
4 People $299
Personal Training Rates:
1 session $102
5 sessions $490
10 sessions $940
20 sessions $1,800
40 sessions $3,400
Please be creative

```html
<!DOCTYPE html>
<html lang="en">
<head>
<meta charset="UTF-8">
<title>Keystride Sports And Fitness – Rates</title>
<link href="https://fonts.googleapis.com/css2?family=Roboto+Condensed:wght@400;500;700&family=Alfa+Slab+One&display=swap" rel="stylesheet">
<style>
  :root {
    --red: #e3101a;
    --red-deep: #b70a12;
    --charcoal: #2e2e30;
    --charcoal-dark: #1c1c1e;
    --silver-light: #f4f4f4;
    --silver: #c9c9cb;
    --ink: #151515;
    --white: #ffffff;
  }
  * { margin: 0; padding: 0; box-sizing: border-box; }
  html, body { width: 800px; height: 1200px; overflow: hidden; background: var(--white); }
  .rate-card {
    position: relative; width: 800px; height: 1200px; overflow: hidden;
    font-family: "Roboto Condensed", Arial, sans-serif; color: var(--white);
  }
  .backdrop { position: absolute; inset: 0; }
  .athlete-photo {
    position: absolute; left: 440px; top: 60px; width: 360px; height: 1140px;
    background: linear-gradient(180deg, rgba(60,60,62,0) 0%, rgba(70,70,74,.55) 20%, rgba(25,25,27,.85) 55%, rgba(20,20,22,.9) 100%);
  }
  .brand { position: absolute; left: 62px; top: 44px; display: flex; align-items: center; gap: 18px; color: var(--red); font-weight: 400; }
  .brand-mark { width: 88px; height: 88px; border-radius: 50%; background: var(--red); }
  .brand-name { font-size: 54px; line-height: 1; letter-spacing: 1px; }
  .brand-tagline { font-size: 15px; letter-spacing: 4px; margin-top: 4px; }
  .membership { position: absolute; left: 70px; top: 222px; width: 330px; text-align: center; }
  .membership-label { color: var(--red); font-size: 38px; font-weight: 500; line-height: 1; }
  .membership-price { font-size: 62px; font-weight: 500; line-height: 1.05; }
  .rate-table { position: absolute; left: 59px; width: 356px; box-shadow: 0 6px 16px rgba(0,0,0,.45); }
  .rate-table.family { top: 435px; }
  .rate-table.training { top: 669px; }
  .rate-heading {
    background: linear-gradient(180deg, var(--red) 0%, var(--red-deep) 100%);
    font-family: "Alfa Slab One", Georgia, serif; font-size: 28px; text-align: center;
    line-height: 1; padding: 12px 10px; letter-spacing: .5px;
  }
  .training .rate-heading { font-size: 27px; padding: 14px 10px 12px; }
  .rate-rows {
    list-style: none; color: var(--ink); font-weight: 700; font-size: 21px;
    background: linear-gradient(180deg, var(--silver-light) 0%, #e6e6e7 55%, var(--silver) 100%);
    padding: 10px 22px 12px 22px;
  }
  .rate-rows li { display: flex; justify-content: space-between; line-height: 44px; }
  .training .rate-rows li { line-height: 41px; }
  .contact { position: absolute; left: 62px; top: 1012px; list-style: none; font-size: 25px; }
  .contact li { display: flex; align-items: center; gap: 14px; line-height: 40px; }
  .contact .address { align-items: flex-start; line-height: 32px; margin-top: 4px; }
  .contact svg { width: 26px; height: 26px; flex: none; }
  .contact .address svg { margin-top: 3px; }
</style>
</head>
<body>
<main class="rate-card">
  <svg class="backdrop" viewBox="0 0 800 1200" preserveAspectRatio="none" aria-hidden="true">
    <defs>
      <linearGradient id="panelShade" x1="0" y1="0" x2="1" y2="1">
        <stop offset="0" stop-color="#3a3a3c"/>
        <stop offset="1" stop-color="#1f1f21"/>
      </linearGradient>
    </defs>
    <rect width="800" height="1200" fill="#ffffff"/>
    <polygon points="0,212 800,118 800,1200 0,1200" fill="url(#panelShade)"/>
    <polygon points="0,196 800,98 800,118 0,212" fill="var(--red)"/>
    <polygon points="560,830 800,760 800,900 560,930" fill="var(--red)"/>
    <polygon points="0,1000 800,900 800,1200 0,1200" fill="var(--red)"/>
  </svg>

  <div class="athlete-photo" role="img" aria-label="Photo of a sprinting female athlete in black sportswear and a red visor"></div>

  <header class="brand">
    <span class="brand-mark"></span>
    <div>
      <div class="brand-name">KEYSTRIDE</div>
      <div class="brand-tagline">SPORTS AND FITNESS</div>
    </div>
  </header>

  <section class="membership">
    <p class="membership-label">MEMBERSHIP</p>
    <p class="membership-price">$99/ MONTH</p>
    <p class="membership-price">$49 HEROES</p>
  </section>

  <section class="rate-table family">
    <h2 class="rate-heading">FAMILY PLAN</h2>
    <ul class="rate-rows">
      <li><span>2 PEOPLE</span><span>$149</span></li>
      <li><span>3 PEOPLE</span><span>$199</span></li>
      <li><span>4 PEOPLE</span><span>$299</span></li>
    </ul>
  </section>

  <section class="rate-table training">
    <h2 class="rate-heading">PERSONAL TRAINING<br>RATES</h2>
    <ul class="rate-rows">
      <li><span>1 SESSION</span><span>$102</span></li>
      <li><span>5 SESSIONS</span><span>$490</span></li>
      <li><span>10 SESSIONS</span><span>$940</span></li>
      <li><span>20 SESSIONS</span><span>$1,800</span></li>
      <li><span>40 SESSIONS</span><span>$3,400</span></li>
    </ul>
  </section>

  <ul class="contact">
    <li>
      <svg viewBox="0 0 24 24" aria-hidden="true"><path fill="#111" d="M6.6 10.8a15 15 0 0 0 6.6 6.6l2.2-2.2a1 1 0 0 1 1-.25 11.4 11.4 0 0 0 3.6.57 1 1 0 0 1 1 1V20a1 1 0 0 1-1 1A17 17 0 0 1 3 4a1 1 0 0 1 1-1h3.5a1 1 0 0 1 1 1c0 1.25.2 2.45.57 3.6a1 1 0 0 1-.25 1z"/></svg>
      <span>703-555-0186</span>
    </li>
    <li>
      <svg viewBox="0 0 24 24" aria-hidden="true"><circle cx="12" cy="12" r="10" fill="#111"/><path d="M2 12h20M12 2c3 3 3 17 0 20M12 2c-3 3-3 17 0 20" stroke="var(--red)" stroke-width="1.4" fill="none"/></svg>
      <span>www.keystridesnf.example</span>
    </li>
    <li class="address">
      <svg viewBox="0 0 24 24" aria-hidden="true"><path fill="#111" d="M12 3 2 12h3v9h5v-6h4v6h5v-9h3z"/></svg>
      <span>2817 Wexley Commerce Dr. Suite 312<br>Chantilly, VA 20418</span>
    </li>
  </ul>
</main>
</body>
</html>
```